Letterhead and Stationary for Construction Company

Lumen Forge needs modern Letterhead, Envelopes and Notepad designs.

Industry/Entity Type

Construction

Colors
f78f20
34a7d8
ffffff

Requirements
Must have
• Modern looking design.

```html
<!DOCTYPE html>
<html lang="en">
<head>
<meta charset="utf-8">
<title>Lumen Forge Stationery</title>
<link href="https://fonts.googleapis.com/css2?family=Roboto:wght@400;500;700&display=swap" rel="stylesheet">
<style>
  :root {
    --bg: #e2e2e2;
    --paper: #ffffff;
    --orange: #f07a28;
    --blue: #1677bf;
    --ink: #4a4a4a;
    --rule: #b9b9b9;
    --shadow: 0 2px 3px rgba(0,0,0,0.28);
  }
  * { box-sizing: border-box; margin: 0; padding: 0; }
  html, body { width: 1200px; height: 960px; overflow: hidden; }
  body { background: var(--bg); font-family: "Roboto", Arial, sans-serif; position: relative; }

  .sheet { position: absolute; background: var(--paper); box-shadow: var(--shadow); overflow: hidden; }
  .brand-bar { position: absolute; left: 0; right: 0; bottom: 0; display: flex; }
  .brand-bar span { flex: 1; }
  .brand-bar .warm { background: var(--orange); }
  .brand-bar .cool { background: var(--blue); }

  .wordmark { position: absolute; display: flex; align-items: center; gap: 6px; font-weight: 500; color: var(--blue); white-space: nowrap; }
  .wordmark .dot { border-radius: 50%; background: var(--orange); flex: none; }
  .wordmark.light { color: var(--paper); }
  .wordmark.light .dot { background: var(--paper); }

  .ghost-ring { position: absolute; border-radius: 50%; border: 10px solid rgba(240,122,40,0.07); }

  /* Letterhead */
  .letterhead { left: 46px; top: 195px; width: 424px; height: 553px; }
  .letterhead .wordmark { left: 34px; top: 36px; font-size: 22px; }
  .letterhead .wordmark .dot { width: 30px; height: 30px; }
  .letterhead .contact { position: absolute; left: 314px; top: 36px; padding-left: 10px; border-left: 1px solid var(--rule); font-size: 5.6px; line-height: 7.4px; color: var(--ink); font-weight: 500; }
  .letterhead .contact .gap { height: 5px; }
  .letterhead .contact .row { display: flex; align-items: center; gap: 3px; }
  .letterhead .contact svg { width: 5px; height: 5px; fill: var(--orange); }
  .letterhead .ghost-ring { left: 320px; top: 437px; width: 100px; height: 100px; }
  .letterhead .brand-bar { height: 9px; }

  /* Envelopes */
  .envelope-back { left: 512px; top: 354px; width: 394px; height: 184px; }
  .envelope-back .flap { position: absolute; left: 0; right: 0; top: 0; height: 58px; background: var(--blue); border-radius: 0 0 14px 14px; clip-path: polygon(0 0, 100% 0, 99% 100%, 1% 100%); }
  .envelope-back .flap-dot { position: absolute; left: 50%; top: 16px; width: 26px; height: 26px; margin-left: -13px; border-radius: 50%; background: var(--paper); }

  .envelope-front { left: 512px; top: 562px; width: 394px; height: 184px; }
  .envelope-front .wordmark { left: 14px; top: 16px; font-size: 15px; gap: 5px; }
  .envelope-front .wordmark .dot { width: 16px; height: 16px; }
  .envelope-front .address { position: absolute; left: 14px; top: 57px; font-size: 5.4px; line-height: 7.4px; color: var(--ink); font-weight: 500; }
  .envelope-front .ghost-ring { left: 254px; top: 18px; width: 140px; height: 140px; border-width: 14px; }
  .envelope-front .brand-bar { height: 8px; }

  /* Notepad */
  .notepad-cover { left: 957px; top: 197px; width: 200px; height: 264px; background: var(--blue); }
  .notepad-cover .texture { position: absolute; inset: 0; background: linear-gradient(160deg, #1a7ec6, #136fb5); }
  .notepad-cover .wordmark { left: 0; right: 0; top: 130px; justify-content: center; font-size: 21px; }
  .notepad-cover .wordmark .dot { width: 18px; height: 18px; }
  .notepad-cover .url { position: absolute; left: 0; right: 0; top: 242px; text-align: center; font-size: 5.6px; letter-spacing: 1.1px; font-weight: 700; color: var(--paper); }

  .notepad-page { left: 957px; top: 486px; width: 200px; height: 264px; }
  .notepad-page .wordmark { left: 0; right: 0; top: 18px; justify-content: center; font-size: 11px; gap: 4px; }
  .notepad-page .wordmark .dot { width: 10px; height: 10px; }
  .notepad-page .lines { position: absolute; left: 16px; right: 16px; top: 57px; height: 177px; background: repeating-linear-gradient(to bottom, var(--rule) 0 1px, transparent 1px 9.8px); }
  .notepad-page .address { position: absolute; left: 0; right: 0; top: 245px; text-align: center; font-size: 5.2px; color: var(--ink); font-weight: 500; }
  .notepad-page .brand-bar { height: 6px; }
</style>
</head>
<body>

<section class="sheet letterhead">
  <div class="wordmark"><span class="dot"></span>Lumen Forge</div>
  <div class="contact">
    <div>12 Foundry Lane, Unit 4</div>
    <div>P.O. Box 210, Millbrook</div>
    <div class="gap"></div>
    <div class="row"><svg viewBox="0 0 10 10"><path d="M2 0.5l2 2-1 1.3a6 6 0 0 0 3.2 3.2L7.5 6l2 2-1.4 1.5C4 9 1 6 0.5 1.9z"/></svg>555-0142-7788</div>
    <div class="row"><svg viewBox="0 0 10 10"><path d="M0 2h10v6H0z M0 2l5 3.5L10 2" /></svg>info@lumenforge.com</div>
    <div class="row"><svg viewBox="0 0 10 10"><circle cx="5" cy="5" r="4.5"/></svg>www.lumenforge.com</div>
  </div>
  <div class="ghost-ring"></div>
  <div class="brand-bar"><span class="warm"></span><span class="cool"></span></div>
</section>

<section class="sheet envelope-back">
  <div class="flap"></div>
  <div class="flap-dot"></div>
</section>

<section class="sheet envelope-front">
  <div class="ghost-ring"></div>
  <div class="wordmark"><span class="dot"></span>Lumen Forge</div>
  <div class="address">
    <div>12 Foundry Lane, Unit 4</div>
    <div>P.O. Box 210, Millbrook</div>
  </div>
  <div class="brand-bar"><span class="warm"></span><span class="cool"></span></div>
</section>

<section class="sheet notepad-cover">
  <div class="texture" role="img" aria-label="Blue cover with a soft repeating brand pattern"></div>
  <div class="wordmark light"><span class="dot"></span>Lumen Forge</div>
  <div class="url">www.lumenforge.com</div>
</section>

<section class="sheet notepad-page">
  <div class="wordmark"><span class="dot"></span>Lumen Forge</div>
  <div class="lines"></div>
  <div class="address">12 Foundry Lane, P.O. Box 210, Millbrook</div>
  <div class="brand-bar"><span class="warm"></span><span class="cool"></span></div>
</section>

</body>
</html>
```